Corvale Enterprises -Business Card Design Project

I have a new logo to put onto business cards - attached
The word doc shows how I want it all laid out - front page and rear
The lettering I want is clean and rounded - modern
Reason: There was no original deadline!
Target Market(s)
25-49 year old leaders and entrepreneurs in Australia
Industry/Entity Type
Business

```html
<!DOCTYPE html>
<html lang="en">
<head>
<meta charset="utf-8">
<title>Corvale Enterprises – Business Card</title>
<link href="https://fonts.googleapis.com/css2?family=Jost:wght@400;500&display=swap" rel="stylesheet">
<style>
  :root {
    --backdrop: #e8e8e8;
    --card: #f9f9f8;
    --brand-blue: #1d4f9c;
    --band-grey: #a9acb0;
    --ink: #1e1e1e;
  }
  * { margin: 0; padding: 0; box-sizing: border-box; }
  html, body { width: 1200px; height: 675px; overflow: hidden; }
  body {
    background: var(--backdrop);
    font-family: "Jost", "Futura", sans-serif;
    color: var(--ink);
    position: relative;
  }
  .card {
    position: absolute;
    top: 188px;
    width: 530px;
    height: 300px;
    background: var(--card);
    box-shadow: 0 2px 6px rgba(0,0,0,0.12);
    overflow: hidden;
  }
  .card--front { left: 45px; }
  .card--back { left: 625px; }

  .edge-bands { position: absolute; left: 0; bottom: 0; width: 530px; height: 90px; }

  .brand {
    position: absolute;
    display: flex;
    align-items: center;
    gap: 10px;
    color: var(--brand-blue);
    font-weight: 500;
    letter-spacing: 0.08em;
    text-transform: uppercase;
  }
  .brand__mark { width: 18px; height: 18px; background: var(--brand-blue); flex: none; }
  .brand__name { font-size: 22px; line-height: 1; }

  /* Front */
  .card--front .brand { left: 70px; top: 62px; }
  .front__tagline {
    position: absolute; left: 0; right: 0; top: 128px;
    text-align: center; font-size: 17px; font-weight: 500;
  }
  .front__name {
    position: absolute; left: 0; right: 0; top: 158px;
    text-align: center; font-size: 19px; font-weight: 500; color: var(--brand-blue);
  }
  .front__role {
    position: absolute; left: 0; right: 0; top: 184px;
    text-align: center; font-size: 12px;
  }

  /* Back */
  .card--back .brand { right: 34px; top: 62px; }
  .back__services {
    position: absolute; left: 34px; top: 92px;
    font-size: 14px; font-weight: 500; line-height: 1.25;
  }
  .back__abn {
    position: absolute; right: 34px; top: 118px;
    font-size: 14px; font-weight: 500;
  }
  .back__contact {
    position: absolute; left: 34px; top: 172px;
    font-size: 14px; font-weight: 500; line-height: 1.3;
    list-style: none;
  }
  .label { color: var(--brand-blue); display: inline-block; width: 52px; }
  .abn-label { color: var(--brand-blue); }
</style>
</head>
<body>

  <section class="card card--front" aria-label="Business card front">
    <div class="brand">
      <span class="brand__mark"></span>
      <span class="brand__name">Corvale Enterprises</span>
    </div>
    <p class="front__tagline">Direction and Growth For Leaders and Entrepreneurs</p>
    <p class="front__name">Declan Hart</p>
    <p class="front__role">Director</p>
    <svg class="edge-bands" viewBox="0 0 530 90" aria-hidden="true">
      <polygon points="300,30 530,6 530,14 330,32" fill="var(--band-grey)"/>
      <polygon points="0,72 530,14 530,30 0,90" fill="var(--brand-blue)"/>
    </svg>
  </section>

  <section class="card card--back" aria-label="Business card back">
    <div class="brand">
      <span class="brand__mark"></span>
      <span class="brand__name">Corvale Enterprises</span>
    </div>
    <p class="back__services">
      NLP Practitioner &amp; Coach<br>
      Personal, Business &amp; Staff Development<br>
      Self Resilience Programs
    </p>
    <p class="back__abn"><span class="abn-label">ABN:</span> 41 207 368 952</p>
    <ul class="back__contact">
      <li><span class="label">Phone:</span> 0412 555 018</li>
      <li><span class="label">Email:</span> declan@corvaleenterprises.com.au</li>
      <li><span class="label">Web:</span> corvaleenterprises.com.au</li>
    </ul>
    <svg class="edge-bands" viewBox="0 0 530 90" aria-hidden="true">
      <polygon points="300,44 530,22 530,32 330,46" fill="var(--band-grey)"/>
      <polygon points="0,78 530,32 530,46 0,90" fill="var(--brand-blue)"/>
    </svg>
  </section>

</body>
</html>
```